Renewable Energy Consultancy needs relatively simple but smart website

We are a renewable energy focussed consultancy called Brenmoss, and we are just starting out. Our target is to bring knowledge of the detailed technical and commercial operations of renewables projects, mainly wind energy.

Our target customers are major energy utilities and private finance groups, who look to invest in renewables projects as a long term money-earning system. We are a fairly young, dynamic team of industry-respected people (4 of us) but we need to make ourselves look bigger than this (our customers will expect us to take on major projects, so we need to look big enough to handle it...)

We're not going to sell anything from our website and we expect it to just support our company name. Most of our customers are made by strong networks and relationships, so its mainly there to give confidence in our capabilities and give a strong view of who we are. We probably need a site with 4/5 pages which we can then expand when needed.

We have logos and headers (attached) which we want to use (also run through quillmarket), and I've attached a few pictures of projects similar to those we will be involved in to give us a feel for how it will look. Also attached are the colours we liked which are now used in the logo, and the font details. Whilst we're a "green" company with a "green" logo, we don't want to be completely green, so some nice combinations of colours on the pages would be good.

Ideally we need to have flenzo/torvaly news feeds somewhere linked into the site.

The design should be smart - giving a feel of high integrity and assurance whilst making us seem approachable and knowledgeable.

Target Market(s)

Renewables investors, developers of renewables projects (wind farms etc),

Industry/Entity Type

Finance

Coding

Coded - Design and coding required

Number of Pages Required

4 page

Other font styles liked:
• See the attachment with brand text/colour details ("colour codes" filename)

Requirements
Must have
• A fairly simple, but smart website design. We're looking to provide confidence and consolidate our networks with the website, not specifically find new customers - so its really just to give customers somewhere they can relate to online
Nice to have
• We have logos/brands and colours - so a website which incorperates these well and brings accross a professional company
• Would be nice to have a page (such as a blog/wordpress) we can easily update with news/events etc and links to flenzo feed and torvaly feed ideally.
Should not have
• cartoons, flashy gimmicks,

```html
<!DOCTYPE html>
<html lang="en">
<head>
<meta charset="utf-8">
<title>Brenmoss Renewables Energy Consultancy</title>
<link rel="stylesheet" href="https://fonts.googleapis.com/css2?family=Open+Sans:ital,wght@0,400;0,600;0,700;1,400;1,600&family=Questrial&display=swap">
<style>
:root{
  --green:#72b000;
  --ink:#1c1c1c;
  --grey:#6d6d6d;
  --white:#ffffff;
  --orange:#e8671c;
}
*{box-sizing:border-box;margin:0;padding:0}
html,body{width:943px;height:1200px;overflow:hidden;background:var(--white)}
body{position:relative;font-family:"Open Sans",Arial,sans-serif;color:var(--ink)}
.abs{position:absolute}

/* header */
.site-header{left:0;top:0;width:943px;height:97px;background:linear-gradient(#f7f9fc,#eef2f7)}
.brand{left:340px;top:18px;height:46px;display:flex;align-items:center;gap:14px}
.brand-mark{width:46px;height:46px;border-radius:50%;background:var(--green)}
.brand-name{font-family:"Questrial",sans-serif;font-size:40px;color:#4a4a4a;letter-spacing:1px}

.main-nav{left:137px;top:79px;width:670px;height:34px;background:var(--white);border-radius:17px;z-index:2;box-shadow:0 1px 3px rgba(0,0,0,.15);overflow:hidden}
.main-nav a{position:absolute;top:0;font-family:"Questrial",sans-serif;font-size:12px;color:#3b3b3b;text-decoration:none;height:34px;line-height:34px;white-space:nowrap}
.main-nav a.active{left:0;width:72px;padding-left:25px;background:var(--green);color:var(--white);border-radius:17px 0 0 17px}

/* hero */
.hero{left:0;top:97px;width:943px;height:431px}
.hero-photo{position:absolute;inset:0;background:linear-gradient(180deg,#7e9fc4 0%,#b7bccb 22%,#d9b9a8 45%,#c9a393 62%,#8d8fa6 78%,#2d3d5c 86%,#1d2c48 100%)}
.hero-title{left:0;top:108px;width:943px;text-align:center;font-weight:700;font-size:44px;line-height:1;color:var(--white)}
.hero-sub{left:0;top:160px;width:943px;text-align:center;font-size:13.5px;line-height:1.2;color:var(--white)}
.cta{left:376px;top:205px;width:151px;height:32px;background:#f7f7f5;border:1px solid #8a8a8a;font-family:"Questrial",sans-serif;font-weight:700;font-size:13px;letter-spacing:.8px;color:#1f3400;display:flex;align-items:center;justify-content:center}
.play{left:546px;top:213px}
.slide-thumb{top:264px;width:115px;height:68px;background:#b5b5b5;padding:6px}
.slide-thumb.current{background:var(--white)}
.slide-thumb span{display:block;width:100%;height:100%}
.thumb-label{top:334px;width:115px;text-align:center;font-size:11.5px;color:rgba(255,255,255,.55)}
.thumb-label.current{color:var(--white)}
.arrow{top:150px;width:32px;height:35px;background:rgba(220,220,220,.8);display:flex;align-items:center;justify-content:center}

/* welcome */
.welcome-title{left:0;top:577px;width:943px;text-align:center;font-family:"Questrial",sans-serif;font-weight:400;font-size:21px;color:var(--ink)}
.welcome-text{left:164px;top:617px;width:615px;text-align:center;font-size:11px;line-height:14.5px;color:var(--ink)}
.welcome-text a{color:var(--orange);text-decoration:none}

/* green band */
.feature-band{left:0;top:717px;width:943px;height:289px;background:var(--green)}
.col-title{font-family:"Questrial",sans-serif;font-weight:400;font-size:16.5px;color:var(--white);letter-spacing:-.3px}
.col-rule{height:2px;background:var(--white)}
.col-rule::after{content:"";position:absolute;left:7px;top:2px;border:4px solid transparent;border-top-color:var(--white)}
.photo-frame{background:var(--white);padding:5px;box-shadow:0 2px 4px rgba(0,0,0,.2)}
.photo-frame span{display:block;width:100%;height:100%}
.caption{font-size:10.3px;color:var(--white)}
.blog-date{font-size:9px;font-style:italic;font-weight:600;color:var(--white)}
.blog-text{font-size:10.8px;line-height:10px;color:var(--white);width:180px}
.view-all{left:665px;top:204px;width:63px;height:16px;background:var(--white);font-size:9px;color:var(--ink);text-align:center;line-height:16px}

/* footer */
.footer-nav{left:0;top:1069px;width:943px;display:flex;justify-content:center;gap:10px}
.footer-nav a{font-size:11.3px;color:var(--grey);text-decoration:none}
.social{left:0;top:1103px;width:943px;display:flex;justify-content:center;gap:14px}
.social a{display:flex;align-items:center;gap:5px;font-size:10px;color:var(--grey);text-decoration:none}
.social i{display:block;width:29px;height:29px;border:1.5px solid var(--grey);border-radius:50%}
.copyright{left:0;top:1152px;width:943px;text-align:center;font-size:11px;color:var(--grey)}
</style>
</head>
<body>

<header class="site-header abs">
  <div class="brand abs"><span class="brand-mark"></span><span class="brand-name">Brenmoss</span></div>
</header>

<nav class="main-nav abs">
  <a class="active" href="#">HOME</a>
  <a href="#" style="left:83px">COMPANY</a>
  <a href="#" style="left:166px">SERVICES</a>
  <a href="#" style="left:240px">PROJECTS</a>
  <a href="#" style="left:319px">RESOURCES</a>
  <a href="#" style="left:407px">NEWS AND EVENTS</a>
  <a href="#" style="left:530px">TEAM</a>
  <a href="#" style="left:584px">CONTACT</a>
</nav>

<section class="hero abs">
  <div class="hero-photo" role="img" aria-label="Offshore wind turbines over the sea under a cloudy sunset sky"></div>
  <h1 class="hero-title abs">Wind Renewables Energy</h1>
  <p class="hero-sub abs">Aliquam sagittis, nibh quis commodo auctor, risus mauris laoreet lectus,facilisis..</p>
  <div class="cta abs">CALL TO ACTION</div>
  <svg class="play abs" width="16" height="16" viewBox="0 0 16 16"><circle cx="8" cy="8" r="6.5" fill="none" stroke="#fff" stroke-width="1.3"/><path d="M6.5 5l4 3-4 3z" fill="#fff"/></svg>

  <div class="slide-thumb abs" style="left:295px"><span role="img" aria-label="Team meeting around a table" style="background:linear-gradient(135deg,#9fb3c8,#e4e6ea 60%,#6f86a8)"></span></div>
  <div class="slide-thumb current abs" style="left:414px"><span role="img" aria-label="Wind turbines under clouds" style="background:linear-gradient(180deg,#7fa0c6,#d5c1b5 60%,#2f4160)"></span></div>
  <div class="slide-thumb abs" style="left:533px"><span role="img" aria-label="Wind turbines at dusk" style="background:linear-gradient(180deg,#2a3f8a,#5d5a9c 50%,#d37a3e 75%,#1f2433)"></span></div>
  <div class="thumb-label abs" style="left:295px">Wind</div>
  <div class="thumb-label current abs" style="left:414px">Wind</div>
  <div class="thumb-label abs" style="left:533px">Lotteries</div>

  <div class="arrow abs" style="left:0"><svg width="12" height="12" viewBox="0 0 12 12"><path d="M8 1.5L3.5 6 8 10.5" fill="none" stroke="#333" stroke-width="2.4"/></svg></div>
  <div class="arrow abs" style="left:911px"><svg width="12" height="12" viewBox="0 0 12 12"><path d="M4 1.5L8.5 6 4 10.5" fill="none" stroke="#333" stroke-width="2.4"/></svg></div>
</section>

<h2 class="welcome-title abs">Welcome to Brenmoss Renewables Energy Consultancy</h2>
<p class="welcome-text abs">Lorem ipsum dolor sit amet, consectetur adipisicing elit, sed do eiusmod tempor incididunt ut labore et dolore magna aliqua. Ut enim ad minim veniam, quis nostrud exercitation ullamco laboris nisi ut aliquip ex ea commodo consequat. Duis aute irure dolor in reprehenderit in voluptate velit esse cillum dolore eu fugiat nulla pariatur. Excepteur sint occaecat cupidatat non proident, <a href="#">Learn More...</a></p>

<section class="feature-band abs">
  <h3 class="col-title abs" style="left:162px;top:45px">Event</h3>
  <div class="col-rule abs" style="left:162px;top:78px;width:168px"></div>
  <div class="photo-frame abs" style="left:162px;top:95px;width:168px;height:102px"><span role="img" aria-label="Turbine installation vessel at port" style="background:linear-gradient(180deg,#a9bfd8,#dfe3e6 55%,#6b4d45 80%,#8d2a25)"></span></div>
  <p class="caption abs" style="left:161px;top:204px">Dated : March 20, 2015</p>

  <h3 class="col-title abs" style="left:355px;top:45px">Our Projects</h3>
  <div class="col-rule abs" style="left:354px;top:78px;width:285px"></div>
  <div class="photo-frame abs" style="left:355px;top:95px;width:138px;height:102px"><span role="img" aria-label="Engineer in orange workwear at an industrial plant" style="background:linear-gradient(120deg,#c76a2c,#9aa3ad 55%,#6f7a86)"></span></div>
  <div class="photo-frame abs" style="left:502px;top:95px;width:137px;height:102px"><span role="img" aria-label="Two engineers in hard hats reviewing plans on site" style="background:linear-gradient(120deg,#c9452f,#c9a13c 45%,#a7b2bd 75%,#7c8894)"></span></div>
  <p class="caption abs" style="left:356px;top:204px">Lorem Project name</p>
  <p class="caption abs" style="left:501px;top:204px">Lorem Project name</p>

  <h3 class="col-title abs" style="left:664px;top:48px">Blogs</h3>
  <div class="col-rule abs" style="left:665px;top:78px;width:168px"></div>
  <p class="blog-date abs" style="left:664px;top:101px">Dated : March 12, 2015</p>
  <p class="blog-text abs" style="left:665px;top:113px">Lorem ipsum dolor sit amet elit aq sed do eiusmod tempor</p>
  <p class="blog-date abs" style="left:664px;top:152px">Dated : March 12, 2015</p>
  <p class="blog-text abs" style="left:665px;top:165px">Lorem ipsum dolor sit amet elit aq sed do eiusmod tempor</p>
  <div class="view-all abs">View All</div>
</section>

<footer>
  <nav class="footer-nav abs">
    <a href="#">Home</a><a href="#">Company</a><a href="#">Services</a><a href="#">Projects</a><a href="#">Resources</a><a href="#">News and Events</a><a href="#">Team</a><a href="#">Contact</a>
  </nav>
  <div class="social abs">
    <a href="#"><i></i>palvora</a>
    <a href="#"><i></i>flenzo</a>
    <a href="#"><i></i>gleamo</a>
  </div>
  <p class="copyright abs">Copyright © 2015</p>
</footer>

</body>
</html>
```